Looking for copywriting of the entire website + new selection of pictures

Hello,
My website's copy write is on the weaker side, so I'm looking for an entire re-do of my website's copy write. If you think a line is weak, re-write, otherwise you can leave it as is. We want our site to clearly explain what our events are, how they work, and why someone should sign up for them, while appealing to the hopeful, romantic, and nostalgic feelings of the visitors. Our speed dating events can be imagined as a modern day approach to the old-fashioned way of dating, where people got to know each other in person, away from the dating apps!! Additionally, I feel nearly all the existing pictures are rather weak, so please select entirely new pictures which give the website a less amateur feel, while retaining the playful nature of the brand. If there are areas where you think that section would benefit from no pictures at all, please communicate that.
Let me know if there are any further questions and thank you!
You can find the site at:
https://www.lanternmeetups.com
Industry/Entity Type
Speed Dating/Romance
Number of Pages Required
1 page
Look and feel
Each slider illustrates characteristics of the customer's brand and the style your logo design should communicate.

```html
<!DOCTYPE html>
<html lang="en">
<head>
<meta charset="utf-8">
<title>Lantern Meetups</title>
<link rel="stylesheet" href="https://fonts.googleapis.com/css2?family=Anton&family=Outfit:wght@400;500&family=Lato:wght@400;700&family=Roboto:wght@400;500&display=swap">
<style>
:root{
  --black:#000;
  --white:#fff;
  --pink:#fbb4d3;
  --pink-soft:#ffc9df;
  --grey:#e8e8e8;
  --ink:#111;
  --pin:#e8473a;
}
*{margin:0;padding:0;box-sizing:border-box}
html,body{width:1200px;height:3094px;overflow:hidden}
body{position:relative;font-family:"Lato",sans-serif;color:var(--ink);background:var(--white)}
section{position:absolute;left:0;width:1200px;overflow:hidden}
.abs{position:absolute}

/* hero */
.hero{top:0;height:607px;background:radial-gradient(ellipse 60% 70% at 25% 60%,#d85a86 0%,#b23a5e 40%,transparent 75%),linear-gradient(100deg,#3a1530 0%,#a53a62 35%,#7a4a8a 65%,#3458a8 100%);color:var(--white);font-family:"Roboto",sans-serif}
.hero::before{content:"";position:absolute;inset:0;background:linear-gradient(180deg,rgba(20,10,25,.85) 0%,rgba(20,10,25,0) 30%)}
.nav a{position:absolute;top:57px;font-size:15px;font-weight:500;color:var(--white);text-decoration:none}
.brand{left:520px;top:55px;width:160px;text-align:center;font-size:17px;font-weight:500;color:var(--white)}
.social{top:55px;width:16px;height:16px;border-radius:50%;background:var(--white)}
.contact{left:1056px;top:44px;width:106px;height:39px;border-radius:10px;background:var(--white);color:var(--black);font-size:15px;font-weight:500;display:flex;align-items:center;justify-content:center}
.hero-photo{left:498px;top:48px;width:589px;height:559px;background:radial-gradient(ellipse at 50% 55%,rgba(214,170,150,.55) 0%,rgba(150,140,160,.35) 50%,transparent 75%)}
.hero-title{left:76px;top:208px;font-family:"Anton",sans-serif;font-size:66px;font-weight:400;line-height:1.1}
.hero-lede{left:76px;top:322px;width:440px;font-size:22px;font-weight:500;line-height:35px}
.hero-list{left:74px;top:432px;list-style:none;font-size:17px;font-weight:500;line-height:34px}
.hero-list li{display:flex;align-items:center;gap:6px}

/* locations */
.locations{top:607px;height:212px;background:var(--pink)}
.section-title{font-family:"Outfit",sans-serif;font-weight:400;text-align:center;width:100%;left:0}
.locations .section-title{top:30px;font-size:46px;font-weight:500}
.city{top:116px;width:258px;height:54px;border-radius:8px;background:var(--white);display:flex;align-items:center;gap:14px;padding-left:18px;font-family:"Roboto",sans-serif;font-size:21px;font-weight:500;text-transform:uppercase}

/* newsletter */
.newsletter{top:819px;height:395px;background:var(--grey)}
.heart-pattern{inset:0;background:radial-gradient(circle at 4% 20%,rgba(240,140,150,.45) 0 32px,transparent 33px),radial-gradient(circle at 96% 20%,rgba(240,140,150,.45) 0 32px,transparent 33px),radial-gradient(circle at 4% 64%,rgba(240,140,150,.45) 0 32px,transparent 33px),radial-gradient(circle at 96% 64%,rgba(240,140,150,.45) 0 32px,transparent 33px)}
.cta-card{left:115px;top:60px;width:970px;height:256px;border-radius:16px;background:var(--black);color:var(--white);text-align:center}
.cta-card h2{font-family:"Outfit",sans-serif;font-weight:500;font-size:48px;margin-top:34px}
.cta-card p{font-size:17px;font-weight:700;margin-top:14px}
.cta-btn{display:inline-block;margin-top:42px;width:140px;height:41px;line-height:41px;border-radius:21px;background:var(--pink-soft);color:var(--black);font-size:12px}

/* intro */
.intro{top:1214px;height:386px;background:var(--pink-soft)}
.intro-photo{left:118px;top:75px;width:475px;height:235px;border-radius:8px;background:linear-gradient(120deg,#6d5a52 0%,#c9b6ad 40%,#e9dcd6 65%,#b9a6a0 100%)}
.intro-text{left:645px;top:106px;font-size:17px;line-height:20px}
.intro-text p{margin-bottom:17px}
.intro-text .name{font-size:19px;font-weight:700;text-decoration:underline;text-underline-offset:3px}

/* how it works */
.how{top:1600px;height:592px;background:var(--grey)}
.how .title{left:115px;top:110px;font-family:"Outfit",sans-serif;font-size:48px;font-weight:400}
.how-steps{left:115px;top:190px;width:470px;font-size:13px;line-height:17px}
.how-steps p{margin-bottom:16px}
.how-photo{left:607px;top:110px;width:480px;height:405px;border-radius:8px;background:linear-gradient(110deg,#7d9bb5 0%,#c9a48d 45%,#e8c8b4 70%,#5a4038 100%)}

/* rounds */
.rounds{top:2192px;height:276px;background:var(--black);color:var(--white)}
.rounds p{left:150px;top:65px;width:900px;text-align:center;font-size:17px;line-height:24px}
.pill{top:158px;width:317px;height:79px;border-radius:10px;background:var(--pink-soft);color:var(--black);display:flex;align-items:center;justify-content:center;font-size:17px;font-weight:700}

/* code */
.code{top:2468px;height:626px;background:var(--pink-soft)}
.code .section-title{top:50px;font-size:48px}
.value{top:158px;width:318px;height:438px;border:1.5px solid var(--black);border-radius:10px;background:var(--white);text-align:center}
.value-icon{display:block;width:90px;height:90px;margin:22px auto 0;border-radius:12px;background:#1a1a1a}
.value h3{font-family:"Roboto",sans-serif;font-weight:500;font-size:30px;margin-top:28px}
.value p{text-align:left;font-size:13px;line-height:20px;margin:28px 40px 0}
</style>
</head>
<body>

<section class="hero">
  <div class="abs hero-photo" role="img" aria-label="Smiling couple embracing, man hugging woman from behind"></div>
  <nav class="nav">
    <a style="left:76px" href="#">Home</a>
    <a style="left:166px" href="#">Event Locations</a>
    <a style="left:323px" href="#">How it Works</a>
    <a style="left:458px" href="#">FAQ</a>
  </nav>
  <div class="abs brand">Lantern Meetups</div>
  <span class="abs social" style="left:922px" aria-label="Social link"></span>
  <span class="abs social" style="left:965px" aria-label="Social link"></span>
  <span class="abs social" style="left:1007px" aria-label="Social link"></span>
  <div class="abs contact">Contact Us</div>
  <h1 class="abs hero-title">Lantern Meetups</h1>
  <p class="abs hero-lede">Old-fashioned romance, reimagined. Meet face to face, away from the apps.</p>
  <ul class="abs hero-list">
    <li><svg width="16" height="14" viewBox="0 0 24 21"><path fill="#fff" d="M12 21 1.8 10.9A6 6 0 0 1 12 2.6a6 6 0 0 1 10.2 8.3Z"/></svg>No hosts, no name tags, just easy, honest conversation</li>
    <li><svg width="16" height="14" viewBox="0 0 24 21"><path fill="#fff" d="M12 21 1.8 10.9A6 6 0 0 1 12 2.6a6 6 0 0 1 10.2 8.3Z"/></svg>Pick an event near you and meet someone real</li>
  </ul>
</section>

<section class="locations">
  <h2 class="abs section-title">Event Locations</h2>
  <div class="abs city" style="left:62px"><svg width="20" height="28" viewBox="0 0 20 28"><path fill="var(--pin)" d="M10 0a10 10 0 0 0-10 10c0 7.5 10 18 10 18s10-10.5 10-18A10 10 0 0 0 10 0Z"/><circle cx="10" cy="10" r="3.6" fill="#fff"/></svg>Boston, MA</div>
  <div class="abs city" style="left:339px"><svg width="20" height="28" viewBox="0 0 20 28"><path fill="var(--pin)" d="M10 0a10 10 0 0 0-10 10c0 7.5 10 18 10 18s10-10.5 10-18A10 10 0 0 0 10 0Z"/><circle cx="10" cy="10" r="3.6" fill="#fff"/></svg>Philadelphia, PA</div>
  <div class="abs city" style="left:615px"><svg width="20" height="28" viewBox="0 0 20 28"><path fill="var(--pin)" d="M10 0a10 10 0 0 0-10 10c0 7.5 10 18 10 18s10-10.5 10-18A10 10 0 0 0 10 0Z"/><circle cx="10" cy="10" r="3.6" fill="#fff"/></svg>Jersey City, NJ</div>
  <div class="abs city" style="left:890px"><svg width="20" height="28" viewBox="0 0 20 28"><path fill="var(--pin)" d="M10 0a10 10 0 0 0-10 10c0 7.5 10 18 10 18s10-10.5 10-18A10 10 0 0 0 10 0Z"/><circle cx="10" cy="10" r="3.6" fill="#fff"/></svg>New York City, NY</div>
</section>

<section class="newsletter">
  <div class="abs heart-pattern" role="img" aria-label="Scattered hand-drawn pink hearts pattern"></div>
  <div class="abs cta-card">
    <h2>Seats Go Fast. Save Yours Today.</h2>
    <p>Join our monthly newsletter and be the first to see every event in your city.</p>
    <span class="cta-btn">CLICK TO JOIN</span>
  </div>
</section>

<section class="intro">
  <div class="abs intro-photo" role="img" aria-label="Couple in winter knitwear, woman holding mittens shaped like a heart"></div>
  <div class="abs intro-text">
    <p>Tired of swiping? 👏</p>
    <p>Remember when people simply met in person?</p>
    <p class="name">Lantern Meetups</p>
    <p>Speed dating as easy as a coffee date</p>
    <p>Find an event near you and meet someone real.</p>
  </div>
</section>

<section class="how">
  <h2 class="abs title">How It Works</h2>
  <div class="abs how-steps">
    <p>No hosts, no name tags - just two people and a <b>real conversation</b></p>
    <p>Your evening is as simple as:</p>
    <p>♥ Arrive at your chosen venue at your set time</p>
    <p>♥ Check your phone for a personal text from us, telling you:</p>
    <p>&nbsp;&nbsp;- When each round starts and ends</p>
    <p>&nbsp;&nbsp;- A short description of your next date</p>
    <p>♥ Spot your date, grab a seat, and start talking!</p>
    <p>♥ When the round ends, text back whether it's a Match! (M) or a Pass (P)</p>
    <p>♥ Repeat, relax, and enjoy the evening!</p>
  </div>
  <div class="abs how-photo" role="img" aria-label="Couple smiling closely, foreheads nearly touching"></div>
</section>

<section class="rounds">
  <p class="abs">♥ Every event has 7 rounds of 10 minutes each. That's long enough to move past small talk and feel a real spark, the way people used to meet. No rushing, no scripts, just an honest conversation with someone new who showed up hoping for the same thing you are.</p>
  <div class="abs pill" style="left:115px">7 Rounds</div>
  <div class="abs pill" style="left:441px">7 Dates</div>
  <div class="abs pill" style="left:768px">7 Chances at a spark</div>
</section>

<section class="code">
  <h2 class="abs section-title">Casual Is Our Code</h2>
  <div class="abs value" style="left:115px">
    <span class="value-icon" role="img" aria-label="Icon of a blazer and a dress"></span>
    <h3>Come As You Are</h3>
    <p>Wear whatever makes you feel like yourself, from office wear straight from work to your favorite cozy sweater. Your style says something about who you are, and that's exactly who your dates want to meet. There are no dress codes and no expectations, just show up and connect.</p>
  </div>
  <div class="abs value" style="left:441px">
    <span class="value-icon" role="img" aria-label="Icon of two chairs with a speech bubble and heart"></span>
    <h3>Real Conversation</h3>
    <p>Your dates are short, so skip the small talk and the resume questions. Save the details for later if you match. Instead, dive into fun, meaningful conversation with the prompts we send you. Whatever the outcome, every date becomes a little story worth telling.</p>
  </div>
  <div class="abs value" style="left:767px">
    <span class="value-icon" role="img" aria-label="Icon of two hearts"></span>
    <h3>Zero Pressure</h3>
    <p>Forget the awkward rituals of typical speed dating and the endless scroll of dating apps. Our events feel like a chat with a friend over coffee: light, warm, and fun. Simply show up, find your date, and enjoy meeting someone new in person.</p>
  </div>
</section>

</body>
</html>
```